Need to create a website for a luxury custom home builder in Phoenix USA. Looking forward for some creative designs including a full page video intro on homepage and should show up pretty luxurious.

```html
<!DOCTYPE html>
<html lang="en">
<head>
<meta charset="UTF-8">
<title>Truenest Homes – Custom Home Experts</title>
<link href="https://fonts.googleapis.com/css2?family=Inter:wght@400;500;600;700;800&display=swap" rel="stylesheet">
<style>
  :root {
    --page-top: #f1f8fd;
    --page-bottom: #dcecf9;
    --brand-blue: #1b8fd6;
    --brand-teal: #18a888;
    --ink: #0d0d0d;
    --muted: #6e6e6e;
    --nav-bg: #f4f4f4;
    --field-top: #fbfbfb;
    --field-bottom: #d9dcdc;
    --label: #3a3a3a;
  }
  * { box-sizing: border-box; margin: 0; padding: 0; }
  html, body { width: 1200px; height: 833px; overflow: hidden; }
  body {
    position: relative;
    font-family: "Inter", sans-serif;
    background: linear-gradient(180deg, var(--page-top) 0%, var(--page-bottom) 100%);
  }
  .brand {
    position: absolute;
    display: flex; align-items: center; gap: 8px;
    font-family: "Inter", sans-serif;
    font-weight: 800;
    color: var(--brand-blue);
    letter-spacing: 0.5px;
    white-space: nowrap;
  }
  .brand-dot { border-radius: 50%; background: var(--brand-blue); }
  .brand--top { left: 50%; top: 92px; transform: translateX(-50%); font-size: 30px; }
  .brand--top .brand-dot { width: 30px; height: 30px; }
  .brand--nav { left: 214px; top: 319px; font-size: 21px; }
  .brand--nav .brand-dot { width: 22px; height: 22px; }

  .tagline {
    position: absolute; left: 0; right: 0; top: 182px;
    text-align: center;
    font-size: 27px; font-weight: 700; line-height: 35px;
    color: var(--muted);
  }

  .site {
    position: absolute; left: 45px; top: 301px;
    width: 1110px; height: 532px;
    overflow: hidden;
    box-shadow: 0 2px 10px rgba(0,0,0,0.08);
  }
  .nav {
    position: absolute; left: 0; top: 0; width: 100%; height: 66px;
    background: var(--nav-bg);
  }
  .nav-link {
    position: absolute; top: 23px;
    font-size: 16px; font-weight: 600; color: var(--ink);
    display: flex; align-items: center; gap: 5px;
  }
  .nav-link svg { width: 12px; height: 12px; }
  .quote-btn {
    position: absolute; left: 806px; top: 10px;
    width: 134px; height: 45px; border-radius: 23px;
    background: var(--brand-blue); color: #fff;
    font-size: 16px; font-weight: 600;
    display: flex; align-items: center; justify-content: center;
  }

  .hero {
    position: absolute; left: 0; top: 66px; width: 100%; height: 466px;
  }
  .hero-photo {
    position: absolute; inset: 0;
    background:
      radial-gradient(ellipse at 20% 15%, #7fa85a 0%, transparent 35%),
      radial-gradient(ellipse at 85% 20%, #6c9a4e 0%, transparent 35%),
      radial-gradient(ellipse at 55% 55%, #e9eeee 0%, transparent 45%),
      radial-gradient(ellipse at 70% 10%, #8c6e5c 0%, transparent 25%),
      linear-gradient(180deg, #c9d6cd 0%, #dfe6e2 60%, #eef3f6 100%);
    filter: blur(2px);
  }
  .hero-fade {
    position: absolute; inset: 0;
    background:
      linear-gradient(90deg, rgba(255,255,255,0.75) 0%, rgba(255,255,255,0.55) 45%, rgba(255,255,255,0) 70%),
      linear-gradient(180deg, rgba(255,255,255,0) 55%, rgba(235,244,250,0.95) 100%);
  }
  .hero-title {
    position: absolute; left: 157px; top: 91px;
    font-size: 43px; font-weight: 700; line-height: 53px;
    color: var(--ink); letter-spacing: -0.3px;
  }
  .hero-sub {
    position: absolute; left: 157px; top: 262px; width: 440px;
    font-size: 17px; font-weight: 600; line-height: 22px; color: var(--ink);
  }
  .explore-btn {
    position: absolute; left: 157px; top: 336px;
    width: 161px; height: 45px; border-radius: 23px;
    background: var(--brand-teal); color: #fff;
    font-size: 16px; font-weight: 600;
    display: flex; align-items: center; justify-content: center;
  }

  .lead-form {
    position: absolute; left: 679px; top: 47px;
    width: 282px; height: 363px;
    background: linear-gradient(180deg, rgba(215,225,222,0.85), rgba(240,244,246,0.9));
    box-shadow: 0 2px 8px rgba(0,0,0,0.15);
  }
  .form-badge {
    position: absolute; left: 261px; top: -22px;
    width: 44px; height: 44px; border-radius: 50%;
    background: #a9acad; border: 2px solid #e6e6e6;
    display: flex; align-items: center; justify-content: center;
  }
  .field-label {
    position: absolute; left: 44px;
    display: flex; align-items: center; gap: 6px;
    font-size: 15px; font-weight: 600; color: var(--label);
  }
  .field-icon {
    width: 18px; height: 18px; border-radius: 50%; background: #6d6d6d;
    display: flex; align-items: center; justify-content: center;
  }
  .field-icon svg { width: 10px; height: 10px; }
  .field {
    position: absolute; left: 44px; width: 193px; height: 41px;
    border-radius: 3px;
    background: linear-gradient(180deg, var(--field-top), var(--field-bottom));
    box-shadow: inset 0 1px 2px rgba(0,0,0,0.2), 0 1px 2px rgba(0,0,0,0.2);
    padding-left: 21px; display: flex; align-items: center;
    font-size: 15px; color: #9a9a9a;
  }
  .priority-btn {
    position: absolute; left: 47px; top: 289px;
    width: 188px; height: 41px; border-radius: 21px;
    background: linear-gradient(180deg, #24b996, #128e75);
    box-shadow: 0 2px 6px rgba(0,0,0,0.3);
    color: #fff; font-size: 15px; font-weight: 700;
    display: flex; align-items: center; justify-content: center;
  }
</style>
</head>
<body>
  <div class="brand brand--top"><span class="brand-dot"></span>TRUENEST HOMES</div>
  <p class="tagline">Crafting Dreams, Building Luxury:<br>Your Custom Home Experts.</p>

  <main class="site">
    <header class="nav">
      <div class="brand brand--nav" style="left:169px;top:18px;"><span class="brand-dot"></span>TRUENEST HOMES</div>
      <span class="nav-link" style="left:425px;">Listings
        <svg viewBox="0 0 12 12"><path d="M2 4l4 4 4-4" fill="none" stroke="#444" stroke-width="1.4"/></svg>
      </span>
      <span class="nav-link" style="left:545px;">Pricing</span>
      <span class="nav-link" style="left:644px;">About</span>
      <span class="quote-btn">Get A Quote</span>
    </header>

    <section class="hero">
      <div class="hero-photo" role="img" aria-label="Blurred aerial view of a modern white luxury home with gardens and pool"></div>
      <div class="hero-fade"></div>
      <h1 class="hero-title">Crafting Dreams.<br>Building Homes.<br>Fulfilling Visions.</h1>
      <p class="hero-sub">Luxury Custom Homes for Sale: Elevating Living in Phoenix, One Dream Home at a Time.</p>
      <span class="explore-btn">Explore Listings</span>

      <form class="lead-form">
        <span class="form-badge">
          <svg width="24" height="24" viewBox="0 0 24 24"><path d="M12 2l3 6.5 7 .8-5.2 4.8 1.5 7L12 17.6 5.7 21.1l1.5-7L2 9.3l7-.8z" fill="#808384"/></svg>
        </span>
        <label class="field-label" style="top:38px;">
          <span class="field-icon"><svg viewBox="0 0 10 10"><circle cx="5" cy="3.2" r="2" fill="#fff"/><path d="M1.2 9.5a3.8 3.8 0 0 1 7.6 0z" fill="#fff"/></svg></span>Name:
        </label>
        <div class="field" style="top:72px;">Name</div>
        <label class="field-label" style="top:114px;">
          <span class="field-icon"><svg viewBox="0 0 10 10"><rect x="1" y="2.2" width="8" height="5.6" fill="none" stroke="#fff" stroke-width="1"/><path d="M1 2.4l4 3 4-3" fill="none" stroke="#fff" stroke-width="1"/></svg></span>Email:
        </label>
        <div class="field" style="top:149px;">Email</div>
        <label class="field-label" style="top:190px;">
          <span class="field-icon"><svg viewBox="0 0 10 10"><path d="M2.2 1l1.7 2-1 1.1a5.5 5.5 0 0 0 3 3L7 6.1l2 1.7-1 1.2C4.5 9 1 5.5 1 2z" fill="#fff"/></svg></span>Phone:
        </label>
        <div class="field" style="top:225px;">Phone</div>
        <span class="priority-btn">Get Priority Access</span>
      </form>
    </section>
  </main>
</body>
</html>
```